Design my Display Ad! Product for Muscle Cramps -- Need Your Talent!

I need the PSD of a square display ad to be the design concept for other ad formats. The product is for leg and muscle cramps. The ad needs to encourage clicks, not simply impressions. Image should contain legs.

Visit www.velmoristride.com for a better idea of the product.

Target Market(s)

People age 55+ with leg cramps

Industry/Entity Type

Health And Wellness

Font styles to use
Sans Serif

Colors

Designer to choose colors to be used in the design.

Requirements
Must have
• One version with the text:
• The Real Cause of Leg Cramps
• Discover the Secret
• The other version with the text:
• Leg Cramps at Night
• Discover the Real Cause
• An image focused on legs.
• Attractive presentation -- this is a premium organic brand.
• Visit www.velmoristride.com for a better understanding of the product

```html
<!DOCTYPE html>
<html lang="en">
<head>
<meta charset="utf-8">
<title>The Real Cause of Leg Cramps – Display Ad</title>
<link rel="stylesheet" href="https://fonts.googleapis.com/css2?family=Montserrat:wght@300;400;700&display=swap">
<style>
  :root {
    --band-light: #4ea6db;
    --band-mid: #3f86b8;
    --band-dark: #346b90;
    --headline: #ffffff;
    --badge: #b8cc55;
    --badge-text: #111111;
    --leg-top: #1a1a1a;
    --leg-bottom: #000000;
  }
  html, body {
    margin: 0;
    padding: 0;
    width: 1200px;
    height: 1200px;
    overflow: hidden;
    background: var(--band-dark);
  }
  .ad {
    position: relative;
    width: 1200px;
    height: 1200px;
    overflow: hidden;
    font-family: "Montserrat", "Helvetica Neue", Arial, sans-serif;
  }
  .ad__backdrop {
    position: absolute;
    inset: 0;
    width: 1200px;
    height: 1200px;
  }
  .ad__headline {
    position: absolute;
    top: 60px;
    left: 0;
    width: 1200px;
    margin: 0;
    text-align: center;
    color: var(--headline);
    font-size: 104px;
    line-height: 158px;
    letter-spacing: 0.03em;
    text-transform: uppercase;
  }
  .ad__headline-strong {
    display: block;
    font-weight: 700;
  }
  .ad__headline-light {
    display: block;
    font-weight: 300;
    margin-top: 8px;
  }
  .ad__leg-visual {
    position: absolute;
    left: 800px;
    top: 390px;
    width: 340px;
    height: 810px;
    border-radius: 120px 40px 0 0;
    background: linear-gradient(180deg, var(--leg-top), var(--leg-bottom));
  }
  .ad__cta {
    position: absolute;
    left: 60px;
    top: 600px;
    width: 516px;
    height: 516px;
    border-radius: 50%;
    background: var(--badge);
    display: flex;
    flex-direction: column;
    align-items: center;
    justify-content: center;
    color: var(--badge-text);
    text-decoration: none;
    font-weight: 400;
    font-size: 76px;
    line-height: 94px;
    letter-spacing: 0.01em;
    text-transform: uppercase;
    text-align: center;
  }
</style>
</head>
<body>
  <main class="ad">
    <svg class="ad__backdrop" viewBox="0 0 1200 1200" aria-hidden="true">
      <rect width="1200" height="1200" fill="var(--band-dark)"/>
      <polygon points="0,0 398,0 848,1200 0,1200" fill="var(--band-mid)"/>
      <polygon points="0,60 412,1200 0,1200" fill="var(--band-light)"/>
    </svg>

    <h1 class="ad__headline">
      <span class="ad__headline-strong">The Real Cause</span>
      <span class="ad__headline-light">of Leg Cramps</span>
    </h1>

    <div class="ad__leg-visual" role="img" aria-label="Black silhouette of a bent leg with small lines marking a cramp at the knee"></div>

    <a class="ad__cta" href="#">
      <span>Discover</span>
      <span>the</span>
      <span>Secret</span>
    </a>
  </main>
</body>
</html>
```